Business Card Trio Design

We need a set of business cards that all match but are not identical. We need one generic for the business and one for each of the two owners. We would like the cards to be similar to each other, but not identical. We have a logo and the colors of the logo are painstakingly chosen so if blue or green is used, we prefer our specific blue and green. Our logo pops better on a black background as well. We are open to double-sided, but it is not the top choice. We would love some either gold or silver accents that are in a foiled appearance. We sell uniforms (scrubs, culinary, EMT, police, fire, business, all types except kids and sports), shoes, equipment, and accessories. We also have facebook, pinterest, instagram, and twitter that we would like to have them follow and we offer splitwell in the store we would like the card to also advertise.

```html
<!DOCTYPE html>
<html lang="en">
<head>
<meta charset="utf-8">
<title>Juniper Workwear Business Cards</title>
<link rel="stylesheet" href="https://fonts.googleapis.com/css2?family=Cinzel:wght@600;700&family=Montserrat:wght@400;500&display=swap">
<style>
  :root {
    --backdrop: #4b4b4a;
    --card: #141414;
    --edge: #0a9a78;
    --brand-blue: #7fa2c4;
    --brand-green: #009b78;
    --ink-light: #f2f2f2;
  }
  * { box-sizing: border-box; margin: 0; padding: 0; }
  html, body { width: 1200px; height: 801px; overflow: hidden; }
  body {
    background: var(--backdrop);
    display: flex;
    align-items: center;
    justify-content: center;
    gap: 48px;
    font-family: "Montserrat", Arial, sans-serif;
  }
  .card {
    position: relative;
    width: 525px;
    height: 300px;
    background: var(--card);
    border-radius: 16px;
    border-bottom: 3px solid var(--edge);
    border-left: 1px solid var(--edge);
    border-right: 1px solid var(--edge);
    overflow: hidden;
  }

  /* Contact side */
  .card--contact { display: flex; align-items: center; padding: 0 34px; }
  .brand-lockup { display: flex; align-items: center; gap: 12px; }
  .brand-lockup__dot {
    width: 46px; height: 46px; border-radius: 50%;
    background: var(--brand-green);
    flex: none;
  }
  .brand-lockup__name {
    font-family: "Cinzel", Georgia, serif;
    font-weight: 700;
    color: var(--brand-blue);
    line-height: 1.05;
    letter-spacing: 0.04em;
  }
  .card--contact .brand-lockup__name { font-size: 22px; }
  .divider {
    width: 1.5px; height: 120px;
    background: var(--brand-green);
    margin: 0 22px;
    flex: none;
  }
  .contact { color: var(--ink-light); }
  .contact__name {
    font-family: "Cinzel", Georgia, serif;
    font-weight: 700;
    color: var(--brand-green);
    font-size: 21px;
    letter-spacing: 0.04em;
  }
  .contact__role { font-size: 12px; margin: 2px 0 16px; }
  .contact__list { list-style: none; font-size: 11.5px; }
  .contact__item { display: flex; align-items: center; gap: 8px; margin-bottom: 5px; }
  .contact__icon { width: 11px; height: 11px; flex: none; }

  /* Brand side */
  .card--brand { display: flex; align-items: center; justify-content: center; }
  .card--brand .brand-lockup { gap: 22px; }
  .card--brand .brand-lockup__dot { width: 110px; height: 110px; }
  .card--brand .brand-lockup__name { font-size: 42px; }
</style>
</head>
<body>
  <section class="card card--contact" aria-label="Owner card, contact side">
    <div class="brand-lockup">
      <span class="brand-lockup__dot"></span>
      <span class="brand-lockup__name">Juniper<br>Workwear</span>
    </div>
    <span class="divider"></span>
    <div class="contact">
      <h1 class="contact__name">Dalton Reeves</h1>
      <p class="contact__role">Owner</p>
      <ul class="contact__list">
        <li class="contact__item">
          <svg class="contact__icon" viewBox="0 0 12 12"><rect x="3" y="0.8" width="6" height="10.4" rx="1" fill="none" stroke="#009b78" stroke-width="1.4"/></svg>
          (555) 014-2281
        </li>
        <li class="contact__item">
          <svg class="contact__icon" viewBox="0 0 12 12"><rect x="3" y="0.8" width="6" height="10.4" rx="1" fill="none" stroke="#009b78" stroke-width="1.4"/></svg>
          (555) 018-6630
        </li>
        <li class="contact__item">
          <svg class="contact__icon" viewBox="0 0 12 12"><rect x="0.5" y="2.5" width="11" height="7.5" fill="#009b78"/><path d="M0.5 2.5 L6 7 L11.5 2.5" fill="none" stroke="#141414" stroke-width="1"/></svg>
          juniperworkwearshop@example.com
        </li>
      </ul>
    </div>
  </section>

  <section class="card card--brand" aria-label="Business card, brand side">
    <div class="brand-lockup">
      <span class="brand-lockup__dot"></span>
      <span class="brand-lockup__name">Juniper<br>Workwear</span>
    </div>
  </section>
</body>
</html>
```